Verdant Holdings Scholarship

Looking to make an attractive scholarship description graphic for my website. Please use the text on the word doc and integrate the two graphics into the layout. Here's what I am looking to replace with the winning design: https://qmeadowllc.example/scholarship-contest/

Thank you

```html
<!DOCTYPE html>
<html lang="en">
<head>
<meta charset="utf-8">
<title>Verdant Holdings Scholarship</title>
<link rel="stylesheet" href="https://fonts.googleapis.com/css2?family=Montserrat:wght@300;500&family=Mrs+Saint+Delafield&family=Cormorant+Garamond:wght@600&display=swap">
<style>
  :root {
    --backdrop: #5b5b5b;
    --paper: #ffffff;
    --brown: #4a3c30;
    --gold: #f5a916;
    --purple: #4b2572;
    --ink: #2b2320;
    --body-text: #3a3a3a;
    --logo-gold: #c9a826;
  }
  * { box-sizing: border-box; margin: 0; padding: 0; }
  html, body {
    width: 1200px; height: 1200px; overflow: hidden;
    background: var(--backdrop);
  }
  .flyer {
    position: absolute; left: 109px; top: 16px;
    width: 1364px; height: 1622px;
    background: var(--paper);
    transform: scale(0.72); transform-origin: top left;
    font-family: "Montserrat", sans-serif; font-weight: 300;
    color: var(--body-text);
  }
  .panels { position: absolute; inset: 0; }
  .hero-photo {
    position: absolute; left: 10px; top: 55px; width: 640px; height: 450px;
    background: radial-gradient(ellipse at 50% 45%, #3b342c 0 30%, #a7b392 45%, #e6e8df 62%, rgba(255,255,255,0) 75%);
  }
  .brand {
    position: absolute; left: 1100px; top: 120px;
    display: flex; align-items: center; gap: 10px;
    font-family: "Montserrat", sans-serif; font-weight: 500;
    font-size: 24px; color: var(--purple);
  }
  .brand-mark { width: 18px; height: 18px; background: var(--purple); }
  .quote {
    position: absolute; left: 675px; top: 235px; width: 620px;
    font-family: "Mrs Saint Delafield", cursive;
    color: var(--ink);
  }
  .quote-lead { font-size: 62px; line-height: 62px; padding-left: 15px; }
  .quote-line { font-size: 40px; line-height: 52px; }
  .quote-author {
    font-family: "Cormorant Garamond", serif; font-weight: 600;
    font-size: 20px; margin-top: 6px; padding-left: 6px;
  }
  .section { position: absolute; font-size: 18px; line-height: 25px; }
  .section h2 { font-weight: 500; font-size: 21px; line-height: 25px; }
  .section ul { list-style: none; }
  .section li { position: relative; padding-left: 52px; }
  .section li::before { content: "•"; position: absolute; left: 0; }
  .on-brown { color: #ffffff; }
  .on-brown h2 { color: #ffffff; }
  .on-gold { color: var(--ink); }
  .on-gold h2 { color: #1a1410; }
  .on-white h2 { color: var(--purple); }
  .on-purple { color: #e6dcef; }
  .on-purple h2 { color: #ffffff; }
  .purpose { left: 160px; top: 622px; width: 380px; }
  .eligibility { left: 781px; top: 622px; width: 450px; }
  .application { left: 160px; top: 968px; width: 470px; }
  .application li { margin-top: 0; }
  .application ul { margin-top: 5px; }
  .scoring { left: 781px; top: 968px; width: 480px; }
  .amount { left: 781px; top: 1168px; width: 480px; }
  .deadline { left: 160px; top: 1408px; width: 1060px; }
  .topic { left: 160px; top: 1508px; width: 1060px; }
</style>
</head>
<body>
  <div class="flyer">
    <svg class="panels" width="1364" height="1622" viewBox="0 0 1364 1622" aria-hidden="true">
      <polygon points="0,468 674,601 674,933 0,933" fill="var(--brown)"/>
      <polygon points="686,601 1364,468 1364,933 686,933" fill="var(--gold)"/>
      <rect x="0" y="1392" width="1364" height="189" fill="var(--purple)"/>
    </svg>

    <div class="hero-photo" role="img" aria-label="Photo of a graduation cap with gold tassel, a rolled diploma with red ribbon and fanned banknotes"></div>

    <div class="brand"><span class="brand-mark"></span>Verdant Holdings</div>

    <div class="quote">
      <p class="quote-lead">“True scholarship</p>
      <p class="quote-line">consists in knowing not what things exist,</p>
      <p class="quote-line">but what they mean;</p>
      <p class="quote-line">it is not memory but judgment.”</p>
      <p class="quote-author">~ Edwin Marlowe Hart.</p>
    </div>

    <section class="section on-brown purpose">
      <h2>Purpose of this Scholarship:</h2>
      <ul>
        <li>To increase trade school, college, and university opportunities of high school seniors</li>
        <li>To encourage high academic achievement in our youth</li>
        <li>To reward hard-working high school seniors and assist in collegiate expenses</li>
      </ul>
    </section>

    <section class="section on-gold eligibility">
      <h2>Eligibility and Requirements at the time of submission for this scholarship:</h2>
      <ul>
        <li>Applicant must be an enrolled high school student in his/her senior year</li>
        <li>Applicant must be in good standing with their high school</li>
        <li>Applicant must have a cumulative grade point average of at least 2.5 on a 4.0 scale</li>
        <li>Applicant must be accepted to a 4-year accredited college, university, trade school or community college</li>
      </ul>
    </section>

    <section class="section on-white application">
      <h2>Application:</h2>
      <p>The application can be submitted via upload on this website, mail (see mailing address below), or scan &amp; email. Email address: pmeadow@qmeadowllc.example. The Application package must include:</p>
      <ul>
        <li>Completed application form</li>
        <li>1 completed scholarship recommendation (teacher, guidance counselor, coach, employer, clergy, NOT friends or family)</li>
        <li>1 Essay no more than 2 pages in length, Times New Roman font (size 12), 1” margins, &amp; double-spaced</li>
        <li>Current high school transcript</li>
        <li>A copy of a College, University, Trade School or Community College acceptance letter</li>
      </ul>
    </section>

    <section class="section on-white scoring">
      <h2>Scoring:</h2>
      <p>The Verdant Holdings Scholarship Scoring Committee will evaluate each application and select ONE winner. If there is a tie, the prize money will be split. The winning essay will be scored based on the grading rubric (Rubric is in downloadable scholarship application packet).</p>
    </section>

    <section class="section on-white amount">
      <h2>Scholarship Amount:</h2>
      <p>The Verdant Holdings Scholarship will award a minimum of $1,500.00 to the winning applicant. Payment will be to the institution that the winner will attend in the fall.</p>
    </section>

    <section class="section on-purple deadline">
      <h2>Deadline:</h2>
      <p>The contest begins on 1 March. Applications postmarked, uploaded, and emailed after 31 May will not be accepted and returned to sender. Verdant Holdings will announce the winner no later than 1 August.</p>
    </section>

    <section class="section on-purple topic">
      <h2>Essay Topic:</h2>
      <p>The essay topic is posted on the last day of February</p>
    </section>
  </div>
</body>
</html>
```